Homepage Hero Image for TradeKip.com

Hi

Our website is TradeKip.com. It is a US based cell phone trade in site. We help users get the most cash when selling their old cell phone , tablet and other electronics

We have redesigned and improved the current website. We just need a new main Hero banner image designing for the homepage before we can put it live

This is a screenshot of the new site showing what needs designing:
https://www.notavelo.com/l/QWrtPzmNb7hKJxLeTyuVBcAsHgUoIdWnRfE

The current hero image in this screenshot looks outdated as it features old phone models and the use of the character also looks outdated

We want a new, fresh design for this main hero image. We would like it to be really bold, modern and up-to-date so that gives a great first impression when a user first lands on the homepage.

The new design can be either illustrative (ie. illustrations of phones) or photography based (ie. photos of phones) but it MUST feature mobile phones and they must be the very latest phone models so the image looks up-to-date. If you use photography based images of phones then please definitely include the latest Zelphon model and latest Vantora model as these brands are the 2 most popular makes eg. https://www.notavelo.com/l/QWmPLKtHzaVBnOe3JrxYwUcSfGdqhIeT2kN

We DON'T want the cartoon man character featured in the new designs

We want a new fresh design as the old design looks outdated but the header text on the old design is fine (ie. "The most cash for your phone guaranteed!"). We still want this as the main message of the new image so you can use this same text or something similar on the new design

You can access the beta version of the new site here:
http://beta.tradekip.com/
USR: tuvo
PWD: Rk4PwzQ8hJ

So that you can create a new hero image in a style that works with the rest of the site here are some good pages to look at :
- http://beta.tradekip.com/cell-phone-trade-in/
- http://beta.tradekip.com/cell-phone-buyback/
- http://beta.tradekip.com/sell/vantora-phone/

We would like a desktop and a mobile version of this new hero banner image but this is a design-only project (no coding) so please just supply one design with how it looks on desktop and one design with how it looks on a mobile

Here are some examples of sites with good quality main homepage hero images we like:
- https://www.brovalink.com/en-gb (especially mobile version of this is very good)
- https://www.moxdrive.co.uk/
- https://ez.com/
- https://drex.com/

If you need anything please just message us

We look forward to receiving your designs!

Target Market(s)

People in the United States looking to sell their old cell phone or other electronics

Industry/Entity Type

Cell Phone

Font styles to use
Sans Serif

Requirements
Must have
• Design MUST feature latest phone models including the latest Zelphon model (QT range) and latest Vantora model (K24 range) as these are the 2 most popular makes people use the site for

```html
<!DOCTYPE html>
<html lang="en">
<head>
<meta charset="utf-8">
<title>TradeKip.com – Homepage Hero, Desktop and Mobile</title>
<link rel="stylesheet" href="https://fonts.googleapis.com/css2?family=Poppins:wght@600;700&display=swap">
<style>
  :root {
    --page: #ffffff;
    --orange-deep: #e64f22;
    --orange-mid: #ee7a3c;
    --orange-light: #f3a067;
    --headline: #e8501f;
    --tagline: #474747;
    --pill: #ffffff;
    --shadow: rgba(0, 0, 0, 0.28);
  }
  * { box-sizing: border-box; margin: 0; padding: 0; }
  html, body {
    width: 1200px; height: 533px; overflow: hidden;
    background: var(--page);
    font-family: "Poppins", "Century Gothic", sans-serif;
  }
  .canvas { position: relative; width: 1200px; height: 533px; }

  .hero {
    position: absolute; overflow: hidden; height: 231px;
    background: linear-gradient(90deg, var(--orange-deep) 0%, var(--orange-mid) 30%, var(--orange-light) 50%, var(--orange-mid) 70%, var(--orange-deep) 100%);
    box-shadow: 0 16px 18px -10px var(--shadow);
  }
  .hero--desktop { left: 0; top: 0; width: 1200px; }
  .hero--mobile { left: 206px; top: 272px; width: 788px; height: 229px; }

  .hero__stage {
    position: absolute; top: 0; left: calc(50% - 600px);
    width: 1200px; height: 231px;
  }
  .hero__curves { position: absolute; inset: 0; }

  .device {
    position: absolute; border-radius: 10px;
    border: 2px solid #2a2a30;
  }
  .device--1 { left: 241px; top: 71px; width: 59px; height: 121px; background: linear-gradient(160deg, #3b3f8f, #e8405a 45%, #f6e2d8 70%, #c93a6a); }
  .device--2 { left: 315px; top: 52px; width: 82px; height: 166px; background: linear-gradient(160deg, #1b2c6a, #2d7fc4 50%, #173a85); border-color: #3a8fd0; }
  .device--3 { left: 414px; top: 40px; width: 111px; height: 200px; background: linear-gradient(135deg, #d9d6e6, #8a7fb0 35%, #0d0d12 60%); border-radius: 14px; }
  .device--4 { left: 540px; top: 7px; width: 127px; height: 230px; background: linear-gradient(170deg, #2a7bd0, #4aa3e6 40%, #7fa7dd 75%, #c7b1dc); border-radius: 14px; }
  .device--5 { left: 682px; top: 41px; width: 108px; height: 196px; background: linear-gradient(160deg, #f0307a, #8a3bb8 45%, #30b3e6 75%, #e2b5e0); border-radius: 12px; }
  .device--6 { left: 805px; top: 54px; width: 75px; height: 161px; background: linear-gradient(170deg, #1f4fb0, #38b6c8 50%, #7fdba0); }
  .device--7 { left: 892px; top: 71px; width: 59px; height: 126px; background: linear-gradient(135deg, #0a0a10 35%, #2a3fa0 60%, #e8d030 80%, #203080); border-radius: 6px; }

  .hero__outline { position: absolute; left: 383px; top: 142px; width: 434px; height: 64px; }

  .hero__headline {
    position: absolute; left: 401px; top: 110px; width: 398px; height: 71px;
    background: var(--pill); border-radius: 20px;
    color: var(--headline); font-weight: 700;
    font-size: 33px; line-height: 27px; letter-spacing: -0.3px;
    text-align: center; padding-top: 9px;
  }
  .hero__headline span { display: block; }
  .hero__headline .line-2 { margin-left: 10px; }

  .hero__tag {
    position: absolute; left: 512px; top: 186px; width: 170px; height: 38px;
    background: var(--pill); border-radius: 14px;
    color: var(--tagline); font-weight: 600; font-size: 22px; line-height: 36px;
    text-align: center; letter-spacing: -0.2px;
  }
</style>
</head>
<body>
<main class="canvas">

  <section class="hero hero--desktop" aria-label="TradeKip.com desktop hero banner">
    <div class="hero__stage">
      <svg class="hero__curves" viewBox="0 0 1200 231" width="1200" height="231" aria-hidden="true">
        <path d="M0 0 L28 0 Q170 160 372 231 L300 231 Q110 160 0 20 Z" fill="#ffffff" fill-opacity="0.14"/>
        <path d="M60 0 Q220 170 372 231" fill="none" stroke="#ffffff" stroke-opacity="0.6" stroke-width="0.7"/>
        <path d="M1200 0 L1172 0 Q1030 160 830 231 L900 231 Q1090 160 1200 20 Z" fill="#ffffff" fill-opacity="0.14"/>
        <path d="M1135 0 Q980 170 830 231" fill="none" stroke="#ffffff" stroke-opacity="0.6" stroke-width="0.7"/>
      </svg>
      <div class="device device--1" role="img" aria-label="Photo of a Zelphon with a colourful lock screen"></div>
      <div class="device device--2" role="img" aria-label="Photo of a blue Zelphon"></div>
      <div class="device device--3" role="img" aria-label="Photo of the latest Zelphon QT"></div>
      <div class="device device--4" role="img" aria-label="Photo of the latest Vantora K24"></div>
      <div class="device device--5" role="img" aria-label="Photo of a Vantora phone with a pink screen"></div>
      <div class="device device--6" role="img" aria-label="Photo of a Vantora phone with a green screen"></div>
      <div class="device device--7" role="img" aria-label="Photo of a Vantora phone with a yellow and blue screen"></div>
      <svg class="hero__outline" viewBox="0 0 434 64" aria-hidden="true">
        <path d="M50 0 Q2 6 2 30 Q2 62 60 62 L420 62 Q432 62 432 30 Q432 6 384 0" fill="none" stroke="#ffffff" stroke-width="0.9"/>
      </svg>
      <h1 class="hero__headline"><span>The most cash for</span><span class="line-2">your phone or tablet</span></h1>
      <p class="hero__tag">guaranteed</p>
    </div>
  </section>

  <section class="hero hero--mobile" aria-label="TradeKip.com mobile hero banner">
    <div class="hero__stage">
      <svg class="hero__curves" viewBox="0 0 1200 231" width="1200" height="231" aria-hidden="true">
        <path d="M206 130 Q290 200 372 231 L300 231 Q250 210 206 180 Z" fill="#ffffff" fill-opacity="0.14"/>
        <path d="M206 150 Q290 205 372 231" fill="none" stroke="#ffffff" stroke-opacity="0.6" stroke-width="0.7"/>
        <path d="M994 130 Q910 200 830 231 L900 231 Q950 210 994 180 Z" fill="#ffffff" fill-opacity="0.14"/>
        <path d="M994 150 Q910 205 830 231" fill="none" stroke="#ffffff" stroke-opacity="0.6" stroke-width="0.7"/>
      </svg>
      <div class="device device--1" role="img" aria-label="Photo of a Zelphon with a colourful lock screen"></div>
      <div class="device device--2" role="img" aria-label="Photo of a blue Zelphon"></div>
      <div class="device device--3" role="img" aria-label="Photo of the latest Zelphon QT"></div>
      <div class="device device--4" role="img" aria-label="Photo of the latest Vantora K24"></div>
      <div class="device device--5" role="img" aria-label="Photo of a Vantora phone with a pink screen"></div>
      <div class="device device--6" role="img" aria-label="Photo of a Vantora phone with a green screen"></div>
      <div class="device device--7" role="img" aria-label="Photo of a Vantora phone with a yellow and blue screen"></div>
      <svg class="hero__outline" viewBox="0 0 434 64" aria-hidden="true">
        <path d="M50 0 Q2 6 2 30 Q2 62 60 62 L420 62 Q432 62 432 30 Q432 6 384 0" fill="none" stroke="#ffffff" stroke-width="0.9"/>
      </svg>
      <p class="hero__headline"><span>The most cash for</span><span class="line-2">your phone or tablet</span></p>
      <p class="hero__tag">guaranteed</p>
    </div>
  </section>

</main>
</body>
</html>
```